Motivational Poster Design Project

I would like to create a poster with some of my favorite quotes to hang in my office.

Industry/Entity Type

Quotes

Requirements
Must have
• The poster will be 24" high x 36" long and printed on canvas, so the image you create needs to have a resolution of at least 2700 x 3900.

The poster must contain the following quotes:

“Your beliefs become your thoughts,
Your thoughts become your words,
Your words become your actions,
Your actions become your habits,
Your habits become your values,
Your values become your destiny.”
-Varuna Pellath

"Winners practice until they get it right. Champions practice until they can’t get it wrong!"
-Unknown

"Style is the perfection of a point of view."
-Conrad Whitlowe

"My interest in life comes from setting myself huge, apparently unachieveable challenges and trying to rise above them."
-Sir Oswin Talbrook

"Problems cannot be solved by the same level of thinking that created them."
-Gustav Morrendel

"People think focus means saying yes to the thing you've got to focus on. But that's not what it means at all. It means saying no to the hundred other good ideas that there are. You have to pick carefully."
-Dale Parrick

"Think like a man of action and act like a man of thought."
-Lucien Marvaud
Nice to have
• It would be nice to have an image of each person who is being quoted (if known) along with the quote that is attributable to them.

```html
<!DOCTYPE html>
<html lang="en">
<head>
<meta charset="utf-8">
<title>Motivation Quote Poster</title>
<link href="https://fonts.googleapis.com/css2?family=Cinzel:wght@400&family=Libre+Baskerville:wght@400;700&family=Playfair+Display:ital@1&display=swap" rel="stylesheet">
<style>
  :root {
    --ink-black: #050608;
    --frame-cyan: #bfe6ec;
    --title-cyan: #b3dfe6;
    --quote-red: #c8142f;
    --quote-navy: #1c2a78;
    --quote-grey: #5a5a5a;
    --quote-dark: #1d1d1d;
    --quote-yellow: #ffe21a;
    --sky-top: #7fc6e6;
    --sky-mid: #b4dce6;
    --horizon: #cfe0b4;
    --sea-teal: #2f9a93;
    --sea-blue: #1f7b9c;
    --sea-deep: #13507f;
    --photo-light: #d2d2d2;
    --photo-mid: #9c9c9c;
    --photo-dark: #4a4a4a;
    --glow: rgba(255,255,255,0.95);
  }
  * { margin: 0; padding: 0; box-sizing: border-box; }
  html, body { width: 1200px; height: 800px; overflow: hidden; background: var(--ink-black); }
  .poster { position: relative; width: 1200px; height: 800px; background: var(--ink-black); }

  .quote-panel {
    position: absolute; left: 66px; top: 62px; width: 1068px; height: 600px;
    border: 1.5px solid var(--frame-cyan); overflow: hidden;
  }
  .seascape {
    position: absolute; inset: 0;
    background: linear-gradient(180deg, var(--sky-top) 0%, var(--sky-mid) 32%, var(--horizon) 46%, var(--sea-teal) 62%, var(--sea-blue) 80%, var(--sea-deep) 100%);
  }
  .portrait {
    position: absolute;
    background: radial-gradient(closest-side, var(--photo-light) 0%, var(--photo-mid) 55%, rgba(156,156,156,0) 100%);
  }
  .portrait--dark {
    background: radial-gradient(closest-side, var(--photo-mid) 0%, var(--photo-dark) 55%, rgba(74,74,74,0) 100%);
  }

  .quote {
    position: absolute; font-family: "Libre Baskerville", Georgia, serif;
    font-size: 17px; line-height: 23px; white-space: nowrap;
    text-shadow: 0 0 4px var(--glow), 0 0 8px var(--glow), 0 0 12px var(--glow);
  }
  .quote .indent { padding-left: 22px; }
  .byline {
    position: absolute; font-family: "Playfair Display", Georgia, serif; font-style: italic;
    font-size: 17px; white-space: nowrap;
    text-shadow: 0 0 4px var(--glow), 0 0 8px var(--glow);
  }
  .red { color: var(--quote-red); }
  .navy { color: var(--quote-navy); }
  .grey { color: var(--quote-grey); }
  .dark { color: var(--quote-dark); }

  .quote--style {
    color: var(--quote-yellow); font-weight: 700; font-size: 22px; line-height: 28px;
    text-shadow: 1px 1px 0 #6a5a00, 0 0 6px rgba(0,0,0,0.5);
  }
  .byline--style { color: var(--quote-yellow); text-shadow: 1px 1px 0 #6a5a00, 0 0 4px rgba(0,0,0,0.5); }

  .title {
    position: absolute; left: 124px; top: 676px; width: 952px;
    display: flex; justify-content: space-between;
    font-family: "Cinzel", "Times New Roman", serif; font-weight: 400; font-size: 92px; line-height: 92px;
    color: var(--title-cyan);
  }
</style>
</head>
<body>
<div class="poster">
  <section class="quote-panel">
    <div class="seascape" role="img" aria-label="Sea under a blue sky at sunset"></div>

    <div class="portrait" role="img" aria-label="Portrait of Varuna Pellath" style="left:0;top:0;width:160px;height:256px"></div>
    <div class="portrait portrait--dark" role="img" aria-label="Portrait of Dale Parrick" style="left:468px;top:0;width:138px;height:250px"></div>
    <div class="portrait" role="img" aria-label="Portrait of Conrad Whitlowe" style="left:870px;top:0;width:160px;height:146px"></div>
    <div class="portrait portrait--dark" role="img" aria-label="Portrait of Lucien Marvaud" style="left:6px;top:362px;width:172px;height:236px"></div>
    <div class="portrait" role="img" aria-label="Portrait of Gustav Morrendel" style="left:440px;top:300px;width:250px;height:215px"></div>
    <div class="portrait" role="img" aria-label="Portrait of Sir Oswin Talbrook" style="left:800px;top:468px;width:260px;height:132px"></div>

    <p class="quote red" style="left:166px;top:16px">“Your beliefs become your<br><span class="indent">thoughts,</span><br>Your thoughts become your<br><span class="indent">words,</span><br>Your words become your actions,<br>Your actions become your habits,<br>Your habits become your values,<br>Your values become your<br><span class="indent">destiny.”</span></p>
    <p class="byline red" style="left:266px;top:224px">-Varuna Pellath</p>

    <p class="quote navy" style="left:610px;top:11px">"People think focus<br>means saying yes to the<br>thing you've got to focus<br>on. But that's not what<br>it means at all. It means<br>saying no to the<br>hundred other good<br>ideas that there are. You<br>have to pick carefully."</p>
    <p class="byline navy" style="left:726px;top:224px">-Dale Parrick</p>

    <p class="quote quote--style" style="left:883px;top:152px">"Style is the<br>perfection of a<br>point of view."</p>
    <p class="byline byline--style" style="left:898px;top:244px">-Conrad Whitlowe</p>

    <p class="quote grey" style="left:110px;top:272px">"Winners practice until they get it<br>right. Champions practice until they<br>can’t get it wrong!"</p>
    <p class="byline grey" style="left:294px;top:337px">-Unknown</p>

    <p class="quote navy" style="left:183px;top:400px;font-size:19px;line-height:28px">"Think like a<br>man of action<br>and act like a<br>man of thought."</p>
    <p class="byline navy" style="left:198px;top:512px">-Lucien Marvaud</p>

    <p class="quote red" style="left:358px;top:519px">"Problems cannot be solved by the same<br>level of thinking that created them."</p>
    <p class="byline red" style="left:574px;top:569px">-Gustav Morrendel</p>

    <p class="quote dark" style="left:694px;top:307px;line-height:26px">"My interest in life comes<br>from setting myself huge,<br>apparently unachieveable<br>challenges and trying to<br>rise above them."</p>
    <p class="byline dark" style="left:718px;top:442px">-Sir Oswin Talbrook</p>
  </section>

  <h1 class="title" aria-label="Motivation">
    <span>M</span><span>O</span><span>T</span><span>I</span><span>V</span><span>A</span><span>T</span><span>I</span><span>O</span><span>N</span>
  </h1>
</div>
</body>
</html>
```